Two companies with one (great) goal... Need a Business card Design

Our Design consists of 2 companies with a common goal-- Embracing a Healthy Lifestyle!
1. The Vitality & Health Travel Trust- consists of a large ranch where horses, and crops of plants and vegetables are a significant component. Tourism developments are underway and the Ffoundation plays a significant role in supporting Sporting events.
2. Pelvaro is a manufacturer of medical and diagnostic equipment inclusive of small medical outposts throughout remote and rural regions of the country.

We are looking for a 2 sided business card with one company on each side. The ideal design will make the 2 different businesses flow together, while at the same time, also work if only one side was printed.

Information for Pelvaro Design:
Medical, Diagnostic and Laboratory Equipment | Medical Imaging NimbusVault ScanHub | Biomedical Services
www.pelvaro-example.bz
info@pelvaro-example.bz
Tel: (555) 382) 9160

Information for The Vitality & Health Travel Trust:
DIRECTOR NAME
Belize, Central America
www.vitalitytrust-example.bz
info@vitalitytrust-example.bz
Tel: (555) 947-2813

*It is important that the font used is not too small please.

A few different color variations of each logo are included, any variation could be used.

Tagline is being finalized but ideally there would be a spot to add this in the future. Top tagline currently is "Healthy Lifestyle Through Better Living"

Industry/Entity Type

Medical

Requirements
Must have
• Font that is large enough to read

```html
<!DOCTYPE html>
<html lang="en">
<head>
<meta charset="utf-8">
<title>Business cards – Vitality &amp; Health Travel Trust / Pelvaro</title>
<link rel="stylesheet" href="https://fonts.googleapis.com/css2?family=Questrial&display=swap">
<style>
  :root {
    --stage: #a4a4a4;
    --card: #fefee0;
    --trust-ink: #6e5c12;
    --trust-accent: #8a6a0c;
    --pelvaro-blue: #1b8fd4;
    --pelvaro-green: #5cb531;
  }
  * { margin: 0; padding: 0; box-sizing: border-box; }
  html, body { width: 1200px; height: 936px; overflow: hidden; }
  body {
    background: var(--stage);
    font-family: "Questrial", "Century Gothic", sans-serif;
    position: relative;
  }
  .card {
    position: absolute;
    background: var(--card);
  }
  .card--trust { left: 106px; top: 200px; width: 566px; height: 346px; color: var(--trust-ink); }
  .card--pelvaro { left: 549px; top: 374px; width: 569px; height: 346px; color: var(--pelvaro-blue); }

  .trust-name {
    position: absolute; left: 0; right: 0; top: 66px;
    text-align: center; font-size: 21px; letter-spacing: 1px; color: var(--trust-ink);
  }
  .director {
    position: absolute; left: 0; right: 0; top: 138px;
    text-align: center; font-size: 30px; color: var(--trust-accent);
  }
  .location {
    position: absolute; left: 0; right: 0; top: 174px;
    text-align: center; font-size: 18px; color: var(--trust-ink);
  }

  .brand {
    position: absolute; left: 0; right: 0; top: 48px;
    display: flex; justify-content: center; align-items: center; gap: 12px;
    font-size: 38px; letter-spacing: 2px; color: var(--pelvaro-blue);
  }
  .brand-square { width: 26px; height: 26px; background: var(--pelvaro-green); }
  .services {
    position: absolute; left: 0; right: 0; top: 116px;
    text-align: center; font-size: 21px; line-height: 28px; text-transform: uppercase;
  }

  .contacts { position: absolute; list-style: none; }
  .card--trust .contacts { left: 138px; top: 236px; }
  .card--pelvaro .contacts { left: 162px; top: 222px; }
  .contacts li { display: flex; align-items: center; height: 30px; font-size: 20px; }
  .contacts svg { width: 20px; height: 20px; margin-right: 12px; fill: currentColor; flex: none; }
  .contacts .phone-line span { margin-left: 18px; }
</style>
</head>
<body>
  <section class="card card--trust" aria-label="The Vitality &amp; Health Travel Trust business card">
    <div class="trust-name">THE VITALITY &amp; HEALTH TRAVEL TRUST</div>
    <div class="director">DIRECTOR NAME</div>
    <div class="location">Belize, Central America</div>
    <ul class="contacts">
      <li><svg viewBox="0 0 20 20"><path d="M10 2 1 10h3v8h5v-5h2v5h5v-8h3z"/></svg>www.vitalitytrust-example.bz</li>
      <li><svg viewBox="0 0 20 20"><path d="M1 4h18v12H1zM3 6v.5l7 5 7-5V6zm0 3v5h14V9l-7 5z"/></svg>info@vitalitytrust-example.bz</li>
      <li class="phone-line"><svg viewBox="0 0 20 20"><path d="M2 6c0-2 3-3 8-3s8 1 8 3v2h-4V6H6v2H2zm3 3h10l3 4v4H2v-4zm5 2a2 2 0 1 0 0 4 2 2 0 0 0 0-4z"/></svg><span>(555) 947-2813</span></li>
    </ul>
  </section>

  <section class="card card--pelvaro" aria-label="Pelvaro business card">
    <div class="brand"><span>PELVARO</span><span class="brand-square"></span></div>
    <div class="services">
      Medical, Diagnostic &amp; Laboratory Equipment<br>
      Medical Imaging NimbusVault ScanHub<br>
      Biomedical Services
    </div>
    <ul class="contacts">
      <li><svg viewBox="0 0 20 20"><path d="M10 2 1 10h3v8h5v-5h2v5h5v-8h3z"/></svg>www.pelvaro-example.bz</li>
      <li><svg viewBox="0 0 20 20"><path d="M1 4h18v12H1zM3 6v.5l7 5 7-5V6zm0 3v5h14V9l-7 5z"/></svg>info@pelvaro-example.bz</li>
      <li class="phone-line"><svg viewBox="0 0 20 20"><path d="M2 6c0-2 3-3 8-3s8 1 8 3v2h-4V6H6v2H2zm3 3h10l3 4v4H2v-4zm5 2a2 2 0 1 0 0 4 2 2 0 0 0 0-4z"/></svg><span>(555) 382) 9160</span></li>
    </ul>
  </section>
</body>
</html>
```